Veteran Owned General Contractor needs Bold New Business Cards

We are a service disabled veteran owned small business. We're a general contractor that specializes in excavation, underground utilities, site work, land clearing and demolition. We would like a fresh, simple, bold, new look for our business cards. We're open to ideas! We'd like to incorporate the following information on the card:

Company Name & Logo, Name of Person, Job Title, Office Phone, Fax, Cell Phone, Email Address, Website, SDVOSB

Our logo is included. We look forward to your thoughts.

Thank you!
Updates

Reason: Hello Due to the overwhelming response to this project, we are extending the deadline one time to allow for improved communication and feedback with the top candidates. We would like to thank everyone for their hard work and exceptional creativity! Thank you

Industry/Entity Type

Business

Contact Information for Business Card

Font styles to use
Sans Serif

Requirements
Nice to have
• As we are a veteran owned company, it would be nice to incorporate an American flag into the design. Maybe on the back?

```html
<!DOCTYPE html>
<html lang="en">
<head>
<meta charset="utf-8">
<title>Baseline7 Inc – Business Cards</title>
<link href="https://fonts.googleapis.com/css2?family=Exo+2:wght@400;500;700;800&display=swap" rel="stylesheet">
<style>
  :root {
    --stage: #1f1f1f;
    --card: #ffffff;
    --green: #5cb83a;
    --green-dark: #4aa22c;
    --grey: #808080;
    --grey-dark: #555555;
    --ink: #3a3a3a;
    --map-tone: #ececec;
  }
  * { box-sizing: border-box; margin: 0; padding: 0; }
  html, body {
    width: 1200px; height: 1000px; overflow: hidden;
    background: var(--stage);
    font-family: "Exo 2", Arial, sans-serif;
  }
  .canvas { position: relative; width: 1200px; height: 1000px; }

  .card {
    position: absolute;
    width: 620px; height: 355px;
    background: var(--card);
    border-radius: 26px;
    overflow: hidden;
  }
  .card--front { left: 70px; top: 90px; }
  .card--back { left: 510px; top: 545px; }

  /* Front */
  .world-map {
    position: absolute; left: 40px; top: 30px; width: 540px; height: 270px;
    background: radial-gradient(ellipse at center, var(--map-tone) 0%, #f6f6f6 60%, var(--card) 100%);
    border-radius: 40px;
  }
  .brand {
    display: flex; align-items: center; gap: 14px;
    color: var(--green); font-weight: 800; letter-spacing: 1px;
  }
  .brand__mark { background: var(--ink); border-radius: 8px; }
  .card--front .brand {
    position: absolute; left: 0; right: 0; top: 0; bottom: 0;
    flex-direction: column; justify-content: center; gap: 22px;
    font-size: 52px;
  }
  .card--front .brand__mark { width: 78px; height: 78px; border-radius: 14px; }

  /* Back */
  .card--back .brand {
    position: absolute; right: 40px; top: 36px; font-size: 36px;
  }
  .card--back .brand__mark { width: 48px; height: 48px; }

  .rule {
    position: absolute; left: 236px; right: 40px; top: 112px;
    height: 2px; background: var(--green);
  }
  .person { position: absolute; left: 40px; top: 128px; }
  .person__name {
    font-size: 34px; font-weight: 800; color: var(--green); letter-spacing: 0.5px;
  }
  .person__title {
    font-size: 19px; color: var(--grey); margin-top: -2px;
    border-top: 2px solid var(--green); display: inline-block; padding-top: 2px;
  }
  .contacts { list-style: none; margin-top: 10px; }
  .contacts li {
    display: flex; align-items: center; gap: 10px;
    font-size: 15px; color: var(--ink); line-height: 21px;
  }
  .contacts svg { width: 14px; height: 14px; fill: var(--green); flex: none; }

  .address {
    position: absolute; right: 40px; top: 132px;
    text-align: right; font-size: 15px; color: var(--ink); line-height: 20px;
  }
  .web-band {
    position: absolute; right: 0; bottom: 40px; width: 230px; height: 38px;
    background: var(--green); border-top-left-radius: 22px;
    color: #fff; font-size: 15px; font-weight: 500;
    display: flex; align-items: center; justify-content: flex-end; padding-right: 30px;
  }
  .stripe { position: absolute; left: 0; right: 0; height: 8px; }
  .stripe--grey { bottom: 26px; background: var(--grey); }
  .stripe--green { bottom: 0; height: 20px; background: var(--green); }
</style>
</head>
<body>
<main class="canvas">

  <section class="card card--front" aria-label="Card front">
    <div class="world-map" role="img" aria-label="Faint grey world map in the background"></div>
    <div class="brand">
      <span class="brand__mark"></span>
      <span class="brand__name">BASELINE7 INC</span>
    </div>
  </section>

  <section class="card card--back" aria-label="Card back">
    <div class="brand">
      <span class="brand__mark"></span>
      <span class="brand__name">BASELINE7 INC</span>
    </div>
    <div class="rule"></div>

    <div class="person">
      <h1 class="person__name">DANIEL REYES</h1>
      <p class="person__title">Ceo &amp; Founder</p>
      <ul class="contacts">
        <li><svg viewBox="0 0 16 16"><path d="M3 1l3 3-2 2c1 2 3 4 5 5l2-2 3 3-2 2C7 14 2 9 1 3z"/></svg>+000 45 10 258</li>
        <li><svg viewBox="0 0 16 16"><path d="M4 0h8v16H4zM5.5 2v10h5V2zM7 13.5h2v1H7z" fill-rule="evenodd"/></svg>+000 85 25 111</li>
        <li><svg viewBox="0 0 16 16"><path d="M4 1h7v4H4zM1 6h14v7H1zM4 11h8v4H4z"/></svg>+000 85 25 122</li>
        <li><svg viewBox="0 0 16 16"><path d="M0 3h16v1L8 9 0 4zM0 6l8 5 8-5v8H0z"/></svg>urname@email.com</li>
      </ul>
    </div>

    <address class="address" style="font-style:normal">Your Street Address,<br>Country, 1234</address>

    <div class="web-band">www.websitename.com</div>
    <div class="stripe stripe--grey"></div>
    <div class="stripe stripe--green"></div>
  </section>

</main>
</body>
</html>
```